Post card for annual skin cancer screening exam

We are looking to design a modern, classy, clean, but fun postcard that we will send out to patients to remind them to schedule their follow up exams for our dermatology office.

It should include our logo
http://tovimek.com/design/logo/jpg/tovimek2.jpg
http://tovimek.com/design/logo/jpg/tovimek.jpg

Address
Phone number
website

We are open to your ideas on wording, as something clever is always appreciated - though this is going to both young and elderly patients - so the message must be easy to read and clear.
Updates

Font styles to use
Serif

Colors
85cae6
3176b5

Requirements
Must have
• Logo
• Office address
• Phone number
• website
• call to action message - to schedule a follow up visit

```html
<!DOCTYPE html>
<html lang="en">
<head>
<meta charset="utf-8">
<title>Tovimek Dermatology – Checkup Reminder Postcard</title>
<link href="https://fonts.googleapis.com/css2?family=Arimo:wght@400;700&display=swap" rel="stylesheet">
<style>
  :root {
    --sky: #85cae6;
    --ocean: #3176b5;
    --ocean-deep: #2a68a3;
    --paper: #ffffff;
    --stage: #eceff2;
    --line: #c9e3f1;
    --photo-light: #e9e2d8;
    --photo-mid: #c9b49c;
  }
  * { box-sizing: border-box; margin: 0; padding: 0; }
  html, body { width: 1200px; height: 483px; overflow: hidden; }
  body {
    background: var(--stage);
    font-family: "Arimo", Arial, sans-serif;
    position: relative;
  }
  .card {
    position: absolute;
    width: 550px;
    height: 388px;
    background: var(--paper);
    overflow: hidden;
    box-shadow: 0 2px 6px rgba(0,0,0,.18);
  }
  .card-front { left: 32px; top: 30px; }
  .card-back { left: 620px; top: 64px; height: 390px; }
  .card-shapes { position: absolute; inset: 0; }

  .brand {
    position: absolute;
    display: flex;
    flex-direction: column;
    align-items: center;
    gap: 10px;
    color: var(--sky);
    font-weight: 400;
    font-size: 22px;
    line-height: 26px;
    letter-spacing: .2px;
    white-space: nowrap;
  }
  .brand-dot {
    width: 30px; height: 30px;
    border-radius: 50%;
    background: var(--sky);
    flex: none;
  }
  .card-front .brand { left: 38px; top: 48px; }
  .card-back .brand { left: 38px; top: 42px; }

  .headline {
    position: absolute;
    left: 46px; top: 212px;
    color: var(--paper);
    font-size: 27px;
    font-weight: 400;
    line-height: 36px;
    letter-spacing: .8px;
  }
  .call-to-action {
    position: absolute;
    left: 44px; top: 330px;
    color: var(--paper);
    font-size: 28px;
    letter-spacing: 1.4px;
  }

  .appointment { position: absolute; left: 34px; top: 122px; }
  .appointment-row {
    display: flex;
    align-items: flex-end;
    height: 30px;
    color: var(--ocean);
    font-size: 16px;
    letter-spacing: .5px;
  }
  .appointment-row .label { width: 56px; padding-bottom: 3px; }
  .appointment-row .fill-line {
    width: 192px;
    border-bottom: 1px solid var(--line);
    margin-bottom: 6px;
  }

  .contact { position: absolute; left: 34px; top: 224px; list-style: none; }
  .contact li {
    display: flex;
    align-items: flex-start;
    gap: 9px;
    color: var(--sky);
    font-size: 12px;
    line-height: 13px;
    letter-spacing: .6px;
    margin-bottom: 8px;
  }
  .contact svg { width: 13px; height: 13px; flex: none; }
</style>
</head>
<body>

<section class="card card-front" aria-label="Postcard front">
  <svg class="card-shapes" viewBox="0 0 550 388" width="550" height="388">
    <defs>
      <radialGradient id="photo-tone" cx="40%" cy="45%" r="70%">
        <stop offset="0" stop-color="var(--photo-light)"/>
        <stop offset="1" stop-color="var(--photo-mid)"/>
      </radialGradient>
    </defs>
    <rect class="colour-band" x="0" y="182" width="550" height="206" fill="var(--ocean)"/>
    <circle cx="412" cy="124" r="138" fill="var(--sky)"/>
    <path d="M276 170 C300 290 470 320 560 240 L560 262 C470 340 300 312 276 170 Z" fill="var(--paper)"/>
    <circle cx="422" cy="124" r="130" fill="var(--paper)"/>
    <circle cx="426" cy="124" r="124" fill="url(#photo-tone)" role="img"
      aria-label="Photo: a dermatologist examining a young woman's arm with a magnifying glass"/>
    <rect x="0" y="384" width="550" height="4" fill="var(--ocean-deep)"/>
  </svg>

  <div class="brand"><span class="brand-dot"></span>Tovimek Dermatology</div>

  <h1 class="headline">Its time for<br>Your chekup</h1>
  <p class="call-to-action">Call us now : (555) 314-2708</p>
</section>

<section class="card card-back" aria-label="Postcard back">
  <svg class="card-shapes" viewBox="0 0 550 390" width="550" height="390">
    <path d="M0 310 C140 276 330 316 470 342 C510 349 540 348 550 344 V390 H0 Z" fill="var(--ocean)"/>
    <path d="M0 330 C150 300 330 336 550 346" fill="none" stroke="var(--paper)" stroke-width="6"/>
  </svg>

  <div class="brand"><span class="brand-dot"></span>Tovimek Dermatology</div>

  <div class="appointment">
    <div class="appointment-row"><span class="label">Date</span><span class="fill-line"></span></div>
    <div class="appointment-row"><span class="label">Time</span><span class="fill-line"></span></div>
    <div class="appointment-row"><span class="label">Place</span><span class="fill-line"></span></div>
  </div>

  <ul class="contact">
    <li>
      <svg viewBox="0 0 16 16" aria-hidden="true"><circle cx="8" cy="8" r="7" fill="none" stroke="var(--ocean)" stroke-width="1.4"/><path d="M5.6 4.4 L6.8 6.2 L6 7 C6.5 8.2 7.6 9.4 9 10 L9.8 9.2 L11.6 10.4 L10.8 11.6 C8 11.4 4.8 8.2 4.4 5.2 Z" fill="var(--ocean)"/></svg>
      (555) 314-2708
    </li>
    <li>
      <svg viewBox="0 0 16 16" aria-hidden="true"><g fill="none" stroke="var(--ocean)" stroke-width="1.2"><circle cx="8" cy="8" r="6.5"/><ellipse cx="8" cy="8" rx="3" ry="6.5"/><path d="M1.5 8 H14.5 M2.6 4.6 H13.4 M2.6 11.4 H13.4"/></g></svg>
      www.tovimek.com
    </li>
    <li>
      <svg viewBox="0 0 16 16" aria-hidden="true"><path d="M8 1 C5 1 3 3.2 3 6 C3 9.6 8 15 8 15 C8 15 13 9.6 13 6 C13 3.2 11 1 8 1 Z" fill="var(--ocean)"/><circle cx="8" cy="6" r="2" fill="var(--paper)"/></svg>
      <span>742 North Meadow Lane;<br>Greenvale NY 10511</span>
    </li>
  </ul>
</section>

</body>
</html>
```